Bluebell Therapy Services needs upgraded website

Upgrade current website www.bluebelltherapy.com.au. Need to incorporate new logo (attached). Family friendly and professional feel. Use of colour green. We are based in Melbourne, Australia and work with children aged 0-16 who have additional needs requiring therapy.

Target Market(s)

Parents of children with special needs.

Industry/Entity Type

Work

Colors
000000

Requirements
Must have
• The current content/ pictures are already on the website and can be replicated, just with a fresh look. Additionally need an FAQ section. Must incorporate logo and have consistency on each page. Needs to be accessible on tablets/devices (current website only shows home page on devices, however actual sites has many sub pages (approx. 7). I will need to be able to easily edit the content down the track and potentially add pages.

```html
<!DOCTYPE html>
<html lang="en">
<head>
<meta charset="utf-8">
<title>Therapy Services – Bluebell Therapy Services</title>
<link rel="stylesheet" href="https://fonts.googleapis.com/css2?family=Open+Sans:wght@400;700&family=PT+Sans:wght@400;700&display=swap">
<style>
:root{
  --page-bg:#d6d6d6;
  --page-band:#e6e6e6;
  --header-green:#9dd9a1;
  --brand-green:#1f6e35;
  --accent-green:#3cb54a;
  --ink:#3d3d3d;
  --muted:#666666;
  --rule:#e2e2e2;
  --tab-bg:#f1f1f1;
  --footer-bg:#393939;
  --white:#ffffff;
}
*{margin:0;padding:0;box-sizing:border-box}
html,body{width:1200px;height:971px;overflow:hidden}
body{
  background:linear-gradient(180deg,var(--page-bg) 0,var(--page-bg) 300px,var(--page-band) 330px,var(--page-bg) 971px);
  font-family:"Open Sans",Arial,sans-serif;color:var(--muted);position:relative;
}
.site{position:absolute;left:292px;top:0;width:613px;height:971px;background:var(--white)}
.abs{position:absolute}

/* header */
.masthead{left:0;top:0;width:613px;height:54px;background:var(--header-green)}
.brand{left:18px;top:10px;display:flex;align-items:center;gap:8px}
.brand-mark{width:22px;height:22px;background:var(--brand-green)}
.brand-name{font-family:"PT Sans",Arial,sans-serif;font-weight:700;font-size:17px;color:var(--brand-green);line-height:1.05;width:150px}
.nav{left:298px;top:0;height:54px;display:flex;gap:0;font-size:9px;color:#2f5b37}
.nav a{color:#2f5b37;text-decoration:none;display:block;padding:20px 0 0}
.nav .item{position:relative;margin-right:22px}
.nav .item.active a{color:var(--white)}
.nav .item.active::before{content:"";position:absolute;left:0;right:0;top:0;height:3px;background:var(--white)}

/* banner */
.banner{left:0;top:54px;width:613px;height:116px;background:linear-gradient(180deg,#e4e4e4 0,#f4f4f4 60%,#d8d8d8 100%)}
.page-title{left:0;top:113px;width:260px;height:44px;background:rgba(255,255,255,.92);font-family:"Open Sans",Arial,sans-serif;font-weight:700;font-size:29px;color:#3b3b3b;padding:2px 0 0 16px;letter-spacing:-.3px}

/* intro */
.intro-photo{left:11px;top:195px;width:273px;height:155px;background:linear-gradient(135deg,#5b3c26,#a47a52 45%,#2c2d38)}
.dots{left:248px;top:334px;display:flex;gap:4px}
.dots span{width:6px;height:6px;border-radius:50%;background:#cfcfcf}
.dots span.on{background:var(--accent-green)}
.section-head{font-family:"PT Sans",Arial,sans-serif;font-size:13px;color:var(--ink);display:flex;align-items:center;gap:24px}
.section-head::after{content:"";flex:1;height:4px;border-top:1px solid var(--rule);border-bottom:1px solid var(--rule)}
.intro-head{left:304px;top:189px;width:288px}
.intro-copy{left:304px;top:221px;width:296px;font-size:7.3px;line-height:12.5px}
.intro-copy p+p{margin-top:12px}

/* tabs */
.ot-head{left:17px;top:384px;width:588px}
.tabs{left:19px;top:408px;width:588px;height:169px;border:1px solid #cfcfcf;border-top:none}
.tab-row{position:absolute;left:-1px;top:0;display:flex}
.tab{height:26px;background:var(--tab-bg);border:1px solid #d3d3d3;font-size:7.5px;color:#555;display:flex;align-items:center;justify-content:center;text-align:center;line-height:9px}
.tab.active{background:var(--white);color:var(--accent-green);border-top:2px solid var(--accent-green);border-bottom-color:var(--white);width:69px}
.tab-line{position:absolute;left:202px;right:-1px;top:25px;border-top:1px solid #cfcfcf}
.tab-copy{position:absolute;left:21px;top:42px;width:545px;font-size:7.3px;line-height:12.5px}
.ticks{position:absolute;left:18px;top:94px;list-style:none;font-size:7.3px}
.ticks li{display:flex;align-items:center;gap:9px;height:21px}
.ticks svg{width:11px;height:11px}

/* accordion */
.divider{left:20px;top:600px;width:570px;height:1px;background:linear-gradient(90deg,transparent,#dcdcdc 20%,#dcdcdc 80%,transparent)}
.services-head{left:31px;top:624px;width:549px}
.accordion{left:29px;top:655px;width:292px;list-style:none}
.accordion li{border-bottom:1px solid var(--rule);font-family:"PT Sans",Arial,sans-serif;font-size:8.2px;color:#2d2d2d}
.acc-title{display:flex;align-items:center;gap:12px;height:31px}
.acc-icon{width:13px;height:12px;background:#2f2f2f;color:#fff;font-size:10px;line-height:11px;text-align:center;font-family:Arial,sans-serif}
.accordion li.open{border-bottom:none}
.accordion li.open .acc-icon{background:var(--accent-green)}
.accordion li.open .acc-title{height:20px}
.acc-body{width:520px;margin-left:25px;font-family:"Open Sans",Arial,sans-serif;font-size:7.3px;line-height:12.5px;color:var(--muted);padding-bottom:4px}

/* footer */
.footer{left:0;top:908px;width:613px;height:63px;background:var(--footer-bg);color:var(--white)}
.footer h3{position:absolute;left:27px;top:21px;font-size:8px;font-weight:700;letter-spacing:.1px}
.footer address{position:absolute;left:27px;top:46px;font-style:normal;font-size:8px;line-height:13px}
.footer .menu-head{left:439px;top:18px;font-size:8px;font-weight:700}
.footer .menu-link{left:439px;top:44px;font-size:8px}
.footer .menu-rule{left:439px;top:62px;width:150px;border-top:1px solid #555}
</style>
</head>
<body>
<div class="site">
  <header class="abs masthead">
    <div class="abs brand">
      <span class="brand-mark"></span>
      <span class="brand-name">Bluebell Therapy Services</span>
    </div>
    <nav class="abs nav">
      <div class="item"><a href="#">Home</a></div>
      <div class="item active"><a href="#">Therapy Services</a></div>
      <div class="item"><a href="#">Staff</a></div>
      <div class="item"><a href="#">FAQ's</a></div>
      <div class="item"><a href="#">Resources</a></div>
      <div class="item"><a href="#">Contact</a></div>
    </nav>
  </header>

  <div class="abs banner" role="img" aria-label="Photo of children in green shirts jumping with arms raised"></div>
  <h1 class="abs page-title">Therapy Services</h1>

  <div class="abs intro-photo" role="img" aria-label="Photo of a therapist working with a young girl at a table of toys"></div>
  <div class="abs dots"><span class="on"></span><span></span></div>
  <h2 class="abs section-head intro-head">Therapy Services</h2>
  <div class="abs intro-copy">
    <p>When a child's ability to be successful is hindered, it can have a dramatic impact on both their self confidence and motivation to persevere. That's where an Occupational Therapist (O.T) comes in. At Bluebell Therapy services we assist children who have a learning, social communication or movement based difficulty to be successful in day to day activities including self care, play, leisure and school life.</p>
    <p>In order to do this O.T's conduct a thorough assessment of the child's performance in functional tasks and identify the particular problem(s) preventing success. We then work with the child, parents and teachers to remediate and/or develop cohesive strategies to optimize performance in these tasks.</p>
  </div>

  <h2 class="abs section-head ot-head">Occupational Therapy</h2>
  <div class="abs tabs">
    <div class="tab-row">
      <div class="tab active">Occupational<br>Therapist</div>
      <div class="tab" style="width:67px">Referals</div>
      <div class="tab" style="width:67px">Daily Skills</div>
    </div>
    <div class="tab-line"></div>
    <p class="tab-copy">An occupational therapist (O.T) sounds like someone you see for help with a job. Well I guess this is true... Children have very important jobs- to play, make friends, be successful at home tasks such as dressing and feeding, and probably most importantly, to reach their social and academic potential.</p>
    <ul class="ticks">
      <li><svg viewBox="0 0 11 11"><circle cx="5.5" cy="5.5" r="5.5" fill="#3cb54a"/><path d="M4.5 3.3 6.7 5.5 4.5 7.7" stroke="#fff" stroke-width="1.4" fill="none"/></svg>Cras rutrum leo at odio volutpat donec fermentum porttitor nunc maecenas quis Etharums ser quidem rerum facilis.</li>
      <li><svg viewBox="0 0 11 11"><circle cx="5.5" cy="5.5" r="5.5" fill="#3cb54a"/><path d="M4.5 3.3 6.7 5.5 4.5 7.7" stroke="#fff" stroke-width="1.4" fill="none"/></svg>Aenean faucibus sapien a odios suspendisse venenatis euismod cras dolores amets unsers fugiats.</li>
    </ul>
  </div>

  <div class="abs divider"></div>
  <h2 class="abs section-head services-head">Bluebell's Therapy Services</h2>
  <ul class="abs accordion">
    <li class="open"><div class="acc-title"><span class="acc-icon">−</span>Fine Motor Coordination</div>
      <p class="acc-body">Fugiat dapibus, tellus ac cursus commodo, mauris sit condim eser ntumsi nibh, uum a justo vitaes amet risus amets un. Posi sectetut amet fermntum orem ipsum quia dolor sit amet, consectetur, adipisci velit, sed quia nons.</p></li>
    <li><div class="acc-title"><span class="acc-icon">+</span>Gross Motor Coordination</div></li>
    <li><div class="acc-title"><span class="acc-icon">+</span>Upper Limb function</div></li>
    <li><div class="acc-title"><span class="acc-icon">+</span>Activities of Daily Living (ADL's)</div></li>
    <li><div class="acc-title"><span class="acc-icon">+</span>Sensory Proccessing</div></li>
    <li><div class="acc-title"><span class="acc-icon">+</span>Perceptual Skills</div></li>
    <li><div class="acc-title"><span class="acc-icon">+</span>Perceptual Skills</div></li>
  </ul>

  <footer class="abs footer">
    <h3>BLUEBELL THERAPY SERVICES</h3>
    <address>P.O.BOX 512 FERNWOOD VIC 3190<br>(03) 9555 0142</address>
    <div class="abs menu-head">MENU</div>
    <div class="abs menu-link">Therapy Services</div>
    <div class="abs menu-rule"></div>
  </footer>
</div>
</body>
</html>
```